Cafe Menu Required

We need a menu for our coffee shop.
I would like something very much the same as what I have attached.

I have attached a word doc with the items needed on the menu.

I have also attached our logo

I would like to print these on A3 size poster

Industry/Entity Type

Cafe

```html
<!DOCTYPE html>
<html lang="en">
<head>
<meta charset="utf-8">
<title>Harbour Brew – Menu</title>
<link href="https://fonts.googleapis.com/css2?family=Oswald:wght@500&family=Pathway+Gothic+One&family=Tangerine:wght@700&display=swap" rel="stylesheet">
<style>
  :root {
    --bg-top: #2e211c;
    --bg-mid: #3a2a23;
    --bg-low: #4a3329;
    --footer: #1d1512;
    --title: #9a7e70;
    --heading: #d6c5ba;
    --text: #dccdc3;
    --rule: #c9b8ad;
    --band: #4b3a37;
    --badge: #2a1f1b;
    --badge-ring: #7d655a;
    --icon: #8e8a88;
  }
  * { margin: 0; padding: 0; box-sizing: border-box; }
  html, body { width: 848px; height: 1200px; overflow: hidden; background: var(--footer); }
  .menu {
    position: relative;
    width: 848px; height: 1200px;
    background:
      radial-gradient(ellipse 70% 18% at 55% 12%, rgba(120,90,75,.28), transparent 70%),
      radial-gradient(ellipse 80% 16% at 40% 80%, rgba(130,95,78,.35), transparent 70%),
      linear-gradient(180deg, var(--bg-top) 0%, var(--bg-mid) 55%, var(--bg-low) 85%, var(--bg-mid) 92%);
    font-family: "Pathway Gothic One", "Arial Narrow", sans-serif;
    color: var(--text);
    overflow: hidden;
  }
  .cup-icon { position: absolute; left: 400px; top: 46px; width: 48px; height: 70px; }
  .title {
    position: absolute; left: 0; top: 136px; width: 848px;
    text-align: center;
    font-family: "Oswald", "Arial Narrow", sans-serif;
    font-weight: 500; font-size: 48px; letter-spacing: 1px;
    color: var(--title);
  }
  .title-rule {
    position: absolute; left: 198px; top: 208px; width: 452px; height: 2px;
    background: linear-gradient(90deg, transparent, var(--rule), transparent);
  }
  .section-heading {
    position: absolute; width: 340px; text-align: center; font-weight: 400;
    font-size: 38px; letter-spacing: 1px; color: var(--heading); top: 278px;
  }
  .section-heading.hot { left: 46px; }
  .section-heading.cold { left: 455px; }
  .column-divider {
    position: absolute; left: 423px; top: 358px; width: 3px; height: 456px;
    background: linear-gradient(180deg, transparent, var(--rule) 15%, var(--rule) 85%, transparent);
  }
  .price-list { position: absolute; list-style: none; font-size: 21px; line-height: 32px; }
  .price-list li { display: flex; }
  .price-list .item { flex: 0 0 auto; }
  .hot-list { left: 73px; top: 358px; }
  .hot-list .item { width: 222px; }
  .cold-list, .extras-list { left: 483px; width: 286px; }
  .cold-list { top: 358px; }
  .extras-list { top: 637px; }
  .cold-list li, .extras-list li { justify-content: space-between; }
  .extras-rule {
    position: absolute; left: 523px; top: 573px; width: 206px; height: 3px;
    background: linear-gradient(90deg, transparent, var(--rule), transparent);
  }
  .extras-heading {
    position: absolute; left: 483px; top: 596px; width: 290px; text-align: center;
    font-family: "Tangerine", cursive; font-weight: 700; font-size: 36px; color: var(--heading);
  }
  .banner-area {
    position: absolute; left: 200px; top: 930px; width: 448px; height: 70px;
    background: linear-gradient(90deg, transparent, var(--band) 25%, var(--band) 75%, transparent);
    opacity: .8;
  }
  .brand-badge {
    position: absolute; left: 324px; top: 876px; width: 200px; height: 200px;
    border-radius: 50%; background: var(--badge); border: 4px solid var(--badge-ring);
    display: flex; align-items: center; justify-content: center;
  }
  .brand-name {
    font-family: "Pathway Gothic One", "Arial Narrow", sans-serif;
    font-size: 38px; letter-spacing: 1px; color: var(--text); text-align: center; line-height: 1;
  }
  .footer { position: absolute; left: 0; top: 1102px; width: 848px; height: 98px; background: var(--footer); }
  .social-links { position: absolute; left: 40px; top: 32px; display: flex; gap: 20px; }
  .social-links span { width: 34px; height: 34px; border-radius: 4px; background: var(--icon); display: block; }
</style>
</head>
<body>
<main class="menu">
  <svg class="cup-icon" viewBox="0 0 48 70" aria-hidden="true">
    <path d="M22 4c-6 6 6 10 0 18 M28 10c-4 5 4 8 0 14" fill="none" stroke="var(--heading)" stroke-width="2.2" stroke-linecap="round"/>
    <path d="M8 40h28v6a14 14 0 0 1-28 0z" fill="var(--heading)"/>
    <path d="M36 43a5 5 0 0 1 0 10" fill="none" stroke="var(--heading)" stroke-width="2.5"/>
    <rect x="4" y="61" width="40" height="3" rx="1.5" fill="var(--heading)"/>
  </svg>

  <h1 class="title">COFFEE – CATERING – FOOD TO GO</h1>
  <div class="title-rule"></div>

  <h2 class="section-heading hot">HOT BEVERAGES</h2>
  <ul class="price-list hot-list">
    <li><span class="item">Espresso</span><span class="price">3.5</span></li>
    <li><span class="item">Piccolo</span><span class="price">3.5</span></li>
    <li><span class="item">Short Macchiato</span><span class="price">4.0</span></li>
    <li><span class="item">Long Macchiato</span><span class="price">4.5</span></li>
    <li><span class="item">Latte</span><span class="price">4/4.5/5.5</span></li>
    <li><span class="item">Cappucinno</span><span class="price">4/4.5/5.5</span></li>
    <li><span class="item">Flat White</span><span class="price">4/4.50/5.50</span></li>
    <li><span class="item">Long Black</span><span class="price">4/4.50/5.50</span></li>
    <li><span class="item">Hot Chocolate</span><span class="price">4/4.50/5.50</span></li>
    <li><span class="item">White Hot Chocolate</span><span class="price">4/4.50/5.50</span></li>
    <li><span class="item">Mocha</span><span class="price">4.5/5.0/6.0</span></li>
    <li><span class="item">White Choc Mocha</span><span class="price">4.5/5.0/6.0</span></li>
    <li><span class="item">Chai Latte</span><span class="price">4.5/5.0/6.0</span></li>
    <li><span class="item">Dirty Chai</span><span class="price">5.0/5.5/6.5</span></li>
    <li><span class="item">Selection of Teas</span><span class="price">3.8</span></li>
  </ul>

  <div class="column-divider"></div>

  <h2 class="section-heading cold">COLD BEVERAGES</h2>
  <ul class="price-list cold-list">
    <li><span class="item">Iced Latte</span><span class="price">4.5</span></li>
    <li><span class="item">Iced Long Black</span><span class="price">4.5</span></li>
    <li><span class="item">Iced Coffee w/ice cream</span><span class="price">6.0</span></li>
    <li><span class="item">Iced Chocolate w/ice cream</span><span class="price">6.0</span></li>
    <li><span class="item">Coffee Frappe</span><span class="price">6.0</span></li>
    <li><span class="item">Mango Frappe</span><span class="price">6.0</span></li>
  </ul>

  <div class="extras-rule"></div>
  <h3 class="extras-heading">Extras</h3>
  <ul class="price-list extras-list">
    <li><span class="item">Extra Shot</span><span class="price">0.5</span></li>
    <li><span class="item">Decaf</span><span class="price">0.5</span></li>
    <li><span class="item">Syrups –</span><span class="price"></span></li>
    <li><span class="item">Caramel/Hazelnut/</span><span class="price"></span></li>
    <li><span class="item">Vanilla</span><span class="price">0.5</span></li>
    <li><span class="item">Soy</span><span class="price">0.5</span></li>
    <li><span class="item">Lactose free</span><span class="price">0.5</span></li>
  </ul>

  <div class="banner-area" role="img" aria-label="Decorative ribbon banner behind the cafe name"></div>

  <div class="brand-badge">
    <span class="brand-name">Harbour<br>Brew</span>
  </div>

  <footer class="footer">
    <div class="social-links" aria-label="Social media">
      <span></span><span></span><span></span>
    </div>
  </footer>
</main>
</body>
</html>
```